Enhance Landing Page

Actual: https://thecoralparlor.com/aposte-em-solaria-lp-port/

I need a better design for this page:
Using this shortcodes : https://sturdy.qvxlayouts.net
Rules:
. Keep the page header
. Keep the footer

```html
<!DOCTYPE html>
<html lang="en">
<head>
<meta charset="utf-8">
<title>Coral Parlor – Landing Page</title>
<link href="https://fonts.googleapis.com/css2?family=Lato:wght@300;400;700&display=swap" rel="stylesheet">
<style>
:root{
  --teal:#5fcdb4;
  --teal-2:#6ccac6;
  --ink:#3b3b3b;
  --muted:#8c8c8c;
  --soft:#f4f4f4;
  --white:#ffffff;
  --dark:#363636;
  --rose:#d8325e;
}
*{box-sizing:border-box;margin:0;padding:0}
html,body{width:1120px;height:1200px;overflow:hidden;background:var(--white)}
body{position:relative;font-family:'Lato',sans-serif;font-weight:300;color:var(--ink)}
.page{position:absolute;background:var(--white);box-shadow:0 6px 24px rgba(0,0,0,.12);overflow:hidden}
.page--home{left:99px;top:50px;width:446px;height:1150px}
.page--more{left:606px;top:0;width:447px;height:1200px}
.section{position:relative;width:100%}
.abs{position:absolute}
.center{left:0;right:0;text-align:center}
.kicker{font-size:5px;color:var(--teal);letter-spacing:.2px}
.heading{font-size:12px;font-weight:300;color:var(--ink);letter-spacing:.4px}
.tiny{font-size:4.3px;line-height:6.4px;color:var(--muted)}
.pill{position:absolute;height:10px;border-radius:6px;font-size:4.4px;font-weight:700;letter-spacing:.3px;color:var(--white);background:var(--teal);display:flex;align-items:center;justify-content:center;text-transform:uppercase}
.photo{position:absolute}

.hero{height:250px}
.hero__photo{inset:0;background:linear-gradient(180deg,#5d7a97 0%,#8aa6bd 40%,#7aa4ad 55%,#cfc3ad 72%,#b9ab94 100%)}
.hero__phones{right:12px;top:6px;font-size:7px;color:#eef2f4;line-height:13.5px;text-align:right}
.flag{display:inline-block;width:6px;height:4px;margin-left:4px;vertical-align:middle}
.hero__title{top:150px;font-size:15px;color:var(--white);line-height:15px;letter-spacing:.2px;font-weight:300}
.hero__title em{font-style:normal;color:var(--rose)}
.hero__cta{left:204px;top:227px;width:54px;height:10px;background:#111;border-radius:6px;font-size:4.4px;color:#fff;display:flex;align-items:center;justify-content:center;letter-spacing:.3px}

.nav{height:32px;background:var(--white)}
.brand{position:absolute;left:33px;top:10px;font-size:9px;font-weight:700;color:var(--ink);letter-spacing:.8px}
.brand__dot{display:inline-block;width:6px;height:6px;border-radius:50%;background:var(--teal);margin-right:4px}
.nav__links{position:absolute;left:165px;top:13px;display:flex;gap:11px;font-size:4.6px;color:var(--ink)}
.nav__links .is-active{color:var(--teal)}

.about{height:324px;background:var(--soft)}
.about__photo{left:62px;top:9px;width:150px;height:159px;background:linear-gradient(180deg,#8fb9d6 0%,#b9d3e0 45%,#7d9aa6 62%,#3d9a9b 78%,#2f8f8a 100%)}
.tabs{position:absolute;left:229px;top:28px;width:180px}
.tab{font-size:5.4px;color:var(--ink);margin-bottom:7px;display:flex;align-items:center}
.tab::before{content:"";width:4px;height:4px;border:0.6px solid #aaa;border-radius:50%;margin-right:6px;flex:none}
.tab.is-open{color:var(--teal)}
.tab.is-open::before{background:var(--teal);border-color:var(--teal)}
.tab__body{margin:-4px 0 8px 10px}
.tab__body p{margin-bottom:5px}
.tab__body i{font-style:italic}
.tab__body a{color:var(--teal)}
.features{position:absolute;left:0;right:0;top:258px}
.feature{position:absolute;width:90px;margin-left:-45px;text-align:center}
.feature svg{display:block;margin:0 auto 6px}
.feature__title{font-size:5.6px;color:var(--ink);margin-bottom:4px}

.promo{height:42px;background:linear-gradient(90deg,var(--teal),var(--teal-2))}
.promo__title{left:63px;top:13px;font-size:9px;color:var(--white)}
.promo__note{left:63px;top:25px;font-size:4px;color:var(--white)}
.promo__btn{left:364px;top:15px;width:45px;height:11px;border:1px solid #fff;border-radius:6px;font-size:4.4px;color:#fff;display:flex;align-items:center;justify-content:center;font-weight:700}

.vision{height:336px;background:var(--white)}
.vision__copy{left:37px;top:79px;width:240px}
.vision__copy strong{display:block;font-size:4.8px;font-weight:700;color:var(--ink);margin-bottom:6px}
.vision__copy a{color:var(--teal)}
.skills{position:absolute;left:291px;top:78px;width:119px}
.skill{position:relative;height:19px;font-size:4.4px;color:var(--ink)}
.skill span{position:absolute;right:16px;top:0}
.skill__track{position:absolute;left:0;right:0;top:9px;height:4px;background:#ececec}
.skill__bar{height:100%;background:var(--teal)}
.service{position:absolute;top:153px;width:90px;margin-left:-45px;text-align:center}
.service__disc{width:85px;height:85px;border-radius:50%;margin:0 auto;background:linear-gradient(180deg,#57b49a 0%,#4d8c80 100%);display:flex;align-items:center;justify-content:center}
.service__tag{font-size:3.6px;color:var(--teal);margin-top:17px;letter-spacing:.3px}
.service__name{font-size:5.6px;color:var(--ink);letter-spacing:.3px}

.stats{height:124px;background:var(--dark)}
.stat{position:absolute;top:42px;width:90px;margin-left:-45px;text-align:center;color:var(--white)}
.stat svg{display:block;margin:0 auto 4px}
.stat__num{font-size:15px;font-weight:300;line-height:16px}
.stat__label{font-size:5.4px;margin-top:3px}

.whatwedo{height:42px;background:var(--soft)}

.portfolio{height:268px;background:var(--soft)}
.tile{position:absolute;width:118px;height:82px;border-top:2px solid var(--teal)}
.tile__caption{position:absolute;left:16px;bottom:-8px;width:86px;height:20px;background:var(--white);text-align:center;padding-top:4px}
.tile__caption b{display:block;font-size:5.4px;font-weight:300;color:var(--ink)}
.tile__caption small{display:block;font-size:3.4px;color:var(--muted);margin-top:1px}

.projects{height:232px;background:var(--white)}
.project{position:absolute;top:70px;width:94px;margin-left:-47px;text-align:center}
.ring{width:48px;height:48px;border:1px solid var(--teal);border-radius:50%;margin:0 auto;display:flex;align-items:center;justify-content:center;font-size:10px;color:var(--teal);position:relative}
.ring::after{content:"";position:absolute;left:-2px;top:26px;width:3px;height:3px;border-radius:50%;background:var(--teal)}
.project__name{font-size:5.4px;color:var(--ink);margin:12px 0 3px}

.testimonials{height:264px;background:var(--soft)}
.quote{position:absolute;top:56px;width:182px}
.quote__photo{position:absolute;left:5px;top:0;width:172px;height:102px}
.quote__text{position:absolute;left:0;top:102px;width:182px;height:64px;background:linear-gradient(90deg,var(--teal),var(--teal-2));padding:12px 20px;font-size:4.2px;line-height:6.6px;color:var(--white)}
.quote__text b{display:block;font-weight:400;margin-top:3px}
.arrow{font-size:8px;color:#aaa}

.offices{height:315px;background:var(--white)}
.map{position:absolute;left:62px;top:100px;width:316px;height:192px;background:linear-gradient(135deg,#63cda5 0%,#66c8bf 100%);border-radius:30% 38% 28% 34%/40% 36% 44% 40%;opacity:.95}
.office{position:absolute;width:92px;height:77px;background:var(--dark);color:var(--white);padding:6px 9px}
.office h4{font-size:5.6px;font-weight:300;margin-bottom:6px}
.office p{font-size:4px;line-height:4.8px;padding-left:9px;position:relative;margin-bottom:4px}
.office p svg{position:absolute;left:0;top:0}
.office__pin{position:absolute;width:5px;height:5px;border-radius:50%;background:#222;border:1px solid #fff}

.contact{height:55px;background:var(--teal)}
.contact__title{left:71px;top:11px;font-size:7px;line-height:8px;font-weight:700;color:var(--dark);letter-spacing:.4px}
.field{position:absolute;top:24px;height:17px;border:1px solid #fff;font-size:5.2px;color:#fff;padding:5px 3px}
.contact__send{left:376px;top:29px;font-size:5.4px;font-weight:700;color:#fff}

.footer{height:66px;background:var(--dark);color:#cfcfcf}
.footer__brand{left:70px;top:42px;font-size:14px;line-height:16px;font-weight:700;color:var(--teal);letter-spacing:1.2px}
.footer__col{position:absolute;top:18px;width:100px}
.footer__col h5{font-size:6.4px;font-weight:300;margin-bottom:7px}
.footer__col p{font-size:4.2px;line-height:6px}
</style>
</head>
<body>

<main class="page page--home">
  <header class="section hero">
    <div class="photo hero__photo" role="img" aria-label="Photo of a palm tree and a beached canoe on a white sand beach by calm sea"></div>
    <div class="abs hero__phones">
      +1 (555)010-4172<span class="flag" style="background:#c94c5a"></span><br>
      +55 21 5550-0142<span class="flag" style="background:#4a9a4e"></span>
    </div>
    <h1 class="abs center hero__title">INVEST IN <em>SOLARIA</em> AND EFFECTIVELY<br>TRANQUILITY</h1>
    <div class="abs hero__cta">LEARN MORE &nbsp;⌄</div>
  </header>

  <nav class="section nav">
    <div class="brand"><span class="brand__dot"></span>CORAL PARLOR</div>
    <div class="nav__links">
      <span>Home</span><span class="is-active">About</span><span>Features</span><span>Opportunities</span><span>Newsletter</span><span>Talk to Agent</span><span>Contact Now</span>
      <svg width="6" height="6" viewBox="0 0 10 10"><circle cx="6" cy="4" r="3" fill="none" stroke="#555"/><path d="M4 6L1 9" stroke="#555"/></svg>
    </div>
  </nav>

  <section class="section about">
    <div class="photo about__photo" role="img" aria-label="Photo of a waterfront city skyline with a tall tower across a turquoise bay"></div>
    <div class="tabs">
      <div class="tab">What We Believe.</div>
      <div class="tab is-open">How We Work.</div>
      <div class="tab__body tiny">
        <p>Clean coastal homes picked with care, quiet streets and bright rooms. Each place is checked by our team before a visit, with fair terms, <a>simple paperwork</a> and a calm move from start to the final key handover.</p>
        <p><i>Good homes near good schools, whatever your plan may be. Local guides help with banks, taxes and permits so every step is clear and nothing is left for later.</i></p>
        <p>Our agents speak your language and answer fast. We keep you informed by phone, mail or video call, with <a>weekly updates</a>.</p>
      </div>
      <div class="tab">Our Passion Is Our Work.</div>
      <div class="tab">Some Other Uber Cool Title.</div>
    </div>

    <div class="abs center kicker" style="top:190px">What makes us Different</div>
    <h2 class="abs center heading" style="top:202px">The Creative Collective</h2>

    <div class="features">
      <div class="feature" style="left:80px">
        <svg width="14" height="14" viewBox="0 0 20 20" fill="none" stroke="#5fcdb4"><path d="M5 2h10v5a5 5 0 01-10 0zM5 4H2a3 3 0 003 4M15 4h3a3 3 0 01-3 4M10 12v4M6 18h8"/></svg>
        <div class="feature__title">The Best of The Best</div>
        <div class="tiny">Solid picks near the coast, clear terms and a fair price.</div>
      </div>
      <div class="feature" style="left:176px">
        <svg width="14" height="14" viewBox="0 0 20 20" fill="none" stroke="#5fcdb4"><path d="M3 17L17 3M3 3l14 14M2 14l4 4M14 2l4 4"/></svg>
        <div class="feature__title">Carefuly Crafted</div>
        <div class="tiny">Solid picks near the coast, clear terms and a fair price.</div>
      </div>
      <div class="feature" style="left:272px">
        <svg width="14" height="14" viewBox="0 0 20 20" fill="none" stroke="#5fcdb4"><path d="M1 17l5-6 4 3 4-7 5-4"/><circle cx="6" cy="11" r="1"/><circle cx="10" cy="14" r="1"/><circle cx="14" cy="7" r="1"/></svg>
        <div class="feature__title">Connect The Dots</div>
        <div class="tiny">Solid picks near the coast, clear terms and a fair price.</div>
      </div>
      <div class="feature" style="left:368px">
        <svg width="14" height="14" viewBox="0 0 20 20" fill="none" stroke="#5fcdb4"><rect x="3" y="8" width="14" height="10"/><path d="M6 8V5a4 4 0 018 0v3M3 12h14M3 15h14"/></svg>
        <div class="feature__title">Solid Work</div>
        <div class="tiny">Solid picks near the coast, clear terms and a fair price.</div>
      </div>
    </div>
  </section>

  <section class="section promo">
    <svg class="abs" style="left:37px;top:11px" width="18" height="17" viewBox="0 0 20 18" fill="none" stroke="#fff"><path d="M10 17S1 11 1 5.5A4.5 4.5 0 0110 4a4.5 4.5 0 019 1.5C19 11 10 17 10 17z"/></svg>
    <div class="abs promo__title">Hire Us Now And Get 50% Discount</div>
    <div class="abs promo__note">*Only first 3 people each day get the discount.</div>
    <div class="abs promo__btn">HIRE US</div>
  </section>

  <section class="section vision">
    <div class="abs center kicker" style="top:27px">How We Roll?</div>
    <h2 class="abs center heading" style="top:44px">360° VISION</h2>
    <div class="abs vision__copy tiny">
      <strong>We take care of absolutely everything to make you feel at home in Solaria!</strong>
      360° service from Brazilian to Brazilian.<br>
      Our specialists will assist you in everything you need to achieve your dream of investing or living in America, with comfort and above all safety . From the choice of the best property to the opening of companies and financial remittances. <a>Grey Kettle</a>
    </div>
    <div class="skills">
      <div class="skill">Awards Earned<span>82%</span><div class="skill__track"><div class="skill__bar" style="width:86%"></div></div></div>
      <div class="skill">Projects Finished<span>69%</span><div class="skill__track"><div class="skill__bar" style="width:75%"></div></div></div>
      <div class="skill">Customer Satisfaction<span>95%</span><div class="skill__track"><div class="skill__bar" style="width:94%"></div></div></div>
    </div>

    <div class="service" style="left:79px">
      <div class="service__disc"><svg width="34" height="48" viewBox="0 0 34 48" fill="none" stroke="#fff" stroke-width="6"><path d="M28 12c-2-4-6-6-11-6-6 0-10 3-10 8 0 11 21 7 21 19 0 5-4 9-11 9-6 0-10-3-12-7M17 0v48"/></svg></div>
      <div class="service__tag">BANK RELATED</div>
      <div class="service__name">FINANCING / REMITTANCES</div>
    </div>
    <div class="service" style="left:175px">
      <div class="service__disc"><svg width="34" height="48" viewBox="0 0 34 48" fill="none" stroke="#fff" stroke-width="4"><rect x="2" y="6" width="30" height="40" rx="4"/><path d="M13 6V2h8v4"/><circle cx="17" cy="22" r="5"/><path d="M8 38c0-6 4-9 9-9s9 3 9 9z" fill="#fff"/></svg></div>
      <div class="service__tag">GREEN CARD</div>
      <div class="service__name">Sen / EB-5</div>
    </div>
    <div class="service" style="left:271px">
      <div class="service__disc"><svg width="50" height="38" viewBox="0 0 50 38" fill="none" stroke="#fff" stroke-width="3.5"><rect x="2" y="8" width="46" height="28" rx="3"/><path d="M18 8V3h14v5M2 18h46"/></svg></div>
      <div class="service__tag">DOCUMENTATION</div>
      <div class="service__name">ACCOUNTING</div>
    </div>
    <div class="service" style="left:367px">
      <div class="service__disc"><svg width="40" height="40" viewBox="0 0 40 40" fill="#fff"><rect x="10" y="2" width="20" height="18" rx="3"/><rect x="2" y="18" width="6" height="10"/><rect x="32" y="18" width="6" height="10"/><rect x="4" y="22" width="32" height="6"/><rect x="6" y="28" width="4" height="10"/><rect x="30" y="28" width="4" height="10"/></svg></div>
      <div class="service__tag">FURNITURE</div>
      <div class="service__name">HOME ADMINISTRATION</div>
    </div>
  </section>

  <section class="section stats">
    <div class="stat" style="left:80px">
      <svg width="16" height="16" viewBox="0 0 20 20" fill="none" stroke="#fff"><circle cx="10" cy="6" r="4"/><path d="M2 19c0-5 4-8 8-8s8 3 8 8"/></svg>
      <div class="stat__num">18</div><div class="stat__label">States</div>
    </div>
    <div class="stat" style="left:176px">
      <svg width="16" height="16" viewBox="0 0 20 20" fill="none" stroke="#fff"><path d="M5 2h10l-1 7a4 4 0 01-8 0zM10 13v5M6 19h8"/></svg>
      <div class="stat__num">40+</div><div class="stat__label">Cities</div>
    </div>
    <div class="stat" style="left:272px">
      <svg width="16" height="16" viewBox="0 0 20 20" fill="none" stroke="#fff"><path d="M10 1a6 6 0 00-4 10c1 1 1 2 1 4h6c0-2 0-3 1-4a6 6 0 00-4-10zM7 17h6M8 19h4"/></svg>
      <div class="stat__num">1945</div><div class="stat__label">Founded</div>
    </div>
    <div class="stat" style="left:368px">
      <svg width="18" height="16" viewBox="0 0 22 18" fill="none" stroke="#fff"><rect x="3" y="1" width="16" height="12"/><path d="M1 16h20"/></svg>
      <div class="stat__num">600</div><div class="stat__label">Under Construction</div>
    </div>
  </section>

  <section class="section whatwedo">
    <div class="abs center kicker" style="top:26px">What We Do?</div>
  </section>
</main>

<main class="page page--more">
  <section class="section portfolio">
    <div class="tile" style="left:37px;top:16px"><div class="photo" style="inset:0;background:linear-gradient(180deg,#5b5f8a,#8d8fb0 50%,#3b8fc0)" role="img" aria-label="Photo of a modern villa with pool at dusk"></div><div class="tile__caption"><b>Vintage Glam Week</b><small>Photography</small></div></div>
    <div class="tile" style="left:164px;top:16px"><div class="photo" style="inset:0;background:linear-gradient(180deg,#e6eaee,#cfd8dc 60%,#b9c8cc)" role="img" aria-label="Photo of a bright white living room"></div><div class="tile__caption"><b>2015 Studio Calendar</b><small>Photography / Graphic Design</small></div></div>
    <div class="tile" style="left:292px;top:16px"><div class="photo" style="inset:0;background:linear-gradient(180deg,#6a5a48,#4f5c5a 60%,#3f4a4a)" role="img" aria-label="Photo of a lounge bar interior"></div><div class="tile__caption"><b>Hipster Were</b><small>Photography / Trend</small></div></div>
    <div class="tile" style="left:37px;top:118px"><div class="photo" style="inset:0;background:linear-gradient(180deg,#8ea3b5,#6d7a7e 50%,#5d6b64)" role="img" aria-label="Aerial photo of a residential neighbourhood"></div><div class="tile__caption"><b>Male Wardrobe</b><small>Photography</small></div></div>
    <div class="tile" style="left:164px;top:118px"><div class="photo" style="inset:0;background:linear-gradient(180deg,#6ea0d6,#a9c6e4 45%,#dfe2e2 70%,#7d8f6a)" role="img" aria-label="Photo of white townhouses under blue sky"></div><div class="tile__caption"><b>Shatelife</b><small>Photography / Trend</small></div></div>
    <div class="tile" style="left:292px;top:118px"><div class="photo" style="inset:0;background:linear-gradient(180deg,#5f95c9,#9cc3da 40%,#5dc3c8 70%,#7fd4cf)" role="img" aria-label="Photo of a resort pool lined with palm trees"></div><div class="tile__caption"><b>Male Fashion</b><small>Fashion</small></div></div>
    <div class="pill" style="left:188px;top:233px;width:72px">Other Opportunities</div>
  </section>

  <section class="section projects">
    <div class="abs center kicker" style="top:30px">What Are We Working On</div>
    <h2 class="abs center heading" style="top:45px">Current Projects</h2>
    <div class="project" style="left:80px"><div class="ring">75%</div><div class="project__name">Miami Hotel</div><div class="tiny">Bright rooms by the sea with new pool and lobby works. Phase two of the tower is now open, ready in early spring.</div></div>
    <div class="project" style="left:177px"><div class="ring">75%</div><div class="project__name">Golf Yard</div><div class="tiny">Bright rooms by the sea with new pool and lobby works. Phase two of the tower is now open, ready in early spring.</div></div>
    <div class="project" style="left:272px"><div class="ring">75%</div><div class="project__name">New Stadium</div><div class="tiny">Bright rooms by the sea with new pool and lobby works. Phase two of the tower is now open, ready in early spring.</div></div>
    <div class="project" style="left:368px"><div class="ring">75%</div><div class="project__name">New Apartements</div><div class="tiny">Bright rooms by the sea with new pool and lobby works. Phase two of the tower is now open, ready in early spring.</div></div>
    <div class="pill" style="left:187px;top:194px;width:72px">Browse Projects &nbsp;›</div>
  </section>

  <section class="section testimonials">
    <div class="abs center kicker" style="top:16px">What our Clients say about us</div>
    <h2 class="abs center heading" style="top:30px">Testimonials</h2>
    <div class="abs arrow" style="left:14px;top:85px">‹</div>
    <div class="abs arrow" style="left:428px;top:85px">›</div>
    <div class="quote" style="left:37px">
      <div class="photo quote__photo" style="background:linear-gradient(180deg,#9aa7b4,#7b848c 50%,#8a5a4a 80%,#6d6f72)" role="img" aria-label="Photo of a smiling woman walking on a city street"></div>
      <div class="quote__text">We found our new home in a few weeks and the team was with us at every step, from the first call to the keys. Clear advice, kind people and no surprise costs along the way.<b>JOHN DOE - www.reviewdesk.net</b></div>
    </div>
    <div class="quote" style="left:228px">
      <div class="photo quote__photo" style="background:linear-gradient(180deg,#5a6a78,#8a9aa6 45%,#c9a79a 75%,#9a8f88)" role="img" aria-label="Photo of a woman with glasses working at an art desk"></div>
      <div class="quote__text">We found our new home in a few weeks and the team was with us at every step, from the first call to the keys. Clear advice, kind people and no surprise costs along the way.<b>JOHN DOE - www.reviewdesk.net</b></div>
    </div>
    <div class="abs arrow" style="left:394px;top:232px;font-size:6px;background:#fff;padding:0 3px">‹ &nbsp;›</div>
  </section>

  <section class="section offices">
    <div class="abs center kicker" style="top:31px">Meet Us Face To Face</div>
    <h2 class="abs center heading" style="top:46px">Our Offices Around The World</h2>
    <div class="map" role="img" aria-label="World map in teal marking the office locations"></div>
    <div class="office" style="left:128px;top:114px">
      <h4>Orlando Office</h4>
      <p><svg width="5" height="5" viewBox="0 0 10 10"><path d="M5 1a3 3 0 00-3 3c0 2 3 5 3 5s3-3 3-5a3 3 0 00-3-3z" fill="none" stroke="#5fcdb4"/></svg>4120 Harbor Lane Avenue,<br>Suite 118, Orlando, USA</p>
      <p><svg width="5" height="5" viewBox="0 0 10 10"><path d="M2 1l2 2-1 2 2 2 2-1 2 2-2 2C4 10 0 6 0 3z" fill="none" stroke="#5fcdb4"/></svg>+1 (555)010-4172</p>
      <p><svg width="5" height="5" viewBox="0 0 10 10"><circle cx="5" cy="5" r="4" fill="none" stroke="#5fcdb4"/><path d="M5 2v3h2" stroke="#5fcdb4" fill="none"/></svg>Mon-Fri: 8 a.m - 8 p.m<br>Sat: 8 a.m - 1 p.m<br>Sun: Closed</p>
    </div>
    <div class="office__pin" style="left:162px;top:194px"></div>
    <div class="office" style="left:162px;top:213px">
      <h4>Orlando Office</h4>
      <p><svg width="5" height="5" viewBox="0 0 10 10"><path d="M5 1a3 3 0 00-3 3c0 2 3 5 3 5s3-3 3-5a3 3 0 00-3-3z" fill="none" stroke="#5fcdb4"/></svg>4120 Harbor Lane Avenue,<br>Suite 118, Orlando, USA</p>
      <p><svg width="5" height="5" viewBox="0 0 10 10"><path d="M2 1l2 2-1 2 2 2 2-1 2 2-2 2C4 10 0 6 0 3z" fill="none" stroke="#5fcdb4"/></svg>+1 (555)010-4172</p>
      <p><svg width="5" height="5" viewBox="0 0 10 10"><circle cx="5" cy="5" r="4" fill="none" stroke="#5fcdb4"/><path d="M5 2v3h2" stroke="#5fcdb4" fill="none"/></svg>Mon-Fri: 8 a.m - 8 p.m<br>Sat: 8 a.m - 1 p.m<br>Sun: Closed</p>
    </div>
  </section>

  <section class="section contact">
    <div class="abs contact__title">CONTACT US DIRECTLY</div>
    <div class="field" style="left:71px;width:55px">Name</div>
    <div class="field" style="left:130px;width:56px">Email</div>
    <div class="field" style="left:192px;width:55px">Phone</div>
    <div class="field" style="left:250px;width:120px">Message</div>
    <div class="abs contact__send">SEND</div>
  </section>

  <footer class="section footer">
    <div class="abs footer__brand">CORAL PARLOR</div>
    <div class="footer__col" style="left:228px">
      <h5>Lagoa Center Barra</h5>
      <p>1° Floor next to the Coffee<br>Sector Av. Marés Altas<br>1200, Praia Serena - RJ -<br>Brazil</p>
    </div>
    <div class="footer__col" style="left:336px">
      <h5>Orlando</h5>
      <p>4120 Harbor Lane Avenue,<br>Suite 118, Orlando, USA<br><br>contact@thecoralparlor.com</p>
    </div>
  </footer>
</main>

</body>
</html>
```